Business card design needed

Our modern electrical contracting company requires business card design utilising our logo and incorporating our tag line "Service when you need it". We specialise in assisting our customers 24/7 offering a breakdown service.

Industry/Entity Type

Electrical

Contact Information for Business Card

Marcus Penhale, Electrical contractor,Tel: (08) 8456 3071, Fax: (08) 8679 4315, Mob 0438 562 740, Email: marcus.penhale@brightwirepower.com.au, Web: www.brightwirepower.com.au

Requirements
Must have
• we require a 2 sided card.
Front- Logo, tag line and contact information.
Rear- service when you need it! Call now for our 24/7 breakdown service

```html
<!DOCTYPE html>
<html lang="en">
<head>
<meta charset="utf-8">
<title>Brightwire Power – Business Card</title>
<link rel="stylesheet" href="https://fonts.googleapis.com/css2?family=Arimo:wght@700&family=Tinos:ital,wght@0,700;1,700&display=swap">
<style>
  :root {
    --brand-blue: #1f55d6;
    --ink: #111111;
    --paper: #ffffff;
  }
  * { margin: 0; padding: 0; box-sizing: border-box; }
  html, body {
    width: 1200px;
    height: 657px;
    overflow: hidden;
    background: var(--paper);
  }
  .card {
    position: relative;
    width: 1200px;
    height: 657px;
    background: var(--paper);
    overflow: hidden;
    font-family: "Tinos", "Times New Roman", serif;
    color: var(--ink);
  }
  .corner-sweep {
    position: absolute;
    left: 0;
    top: 0;
    width: 1200px;
    height: 657px;
  }
  .corner-sweep path { fill: var(--brand-blue); }

  .holder {
    position: absolute;
    left: 640px;
    width: 562px;
    top: 130px;
    text-align center;
    text-align: center;
    color: var(--paper);
  }
  .holder-name {
    font-weight: 700;
    font-size: 52px;
    line-height: 1;
    letter-spacing: 0.5px;
  }
  .holder-role {
    font-weight: 700;
    font-style: italic;
    font-size: 33px;
    line-height: 1;
    margin-top: 16px;
  }

  .brand-mark {
    position: absolute;
    left: 0;
    top: 0;
    width: 1200px;
    height: 657px;
    pointer-events: none;
  }
  .brand-dot { fill: var(--brand-blue); }
  .brand-name {
    fill: var(--brand-blue);
    font-family: "Arimo", Arial, sans-serif;
    font-weight: 700;
    font-size: 84px;
  }

  .tagline {
    position: absolute;
    left: 95px;
    width: 600px;
    top: 417px;
    text-align: center;
    font-weight: 700;
    font-style: italic;
    font-size: 37px;
    line-height: 1;
  }

  .contact {
    position: absolute;
    left: 0;
    width: 1114px;
    top: 518px;
    text-align: center;
    font-weight: 700;
    font-style: italic;
    font-size: 37px;
    line-height: 46px;
    white-space: nowrap;
  }
</style>
</head>
<body>
  <main class="card">
    <svg class="corner-sweep" viewBox="0 0 1200 657" aria-hidden="true">
      <path d="M627,0 C640,170 760,320 960,375 C1050,395 1130,395 1200,392 L1200,0 Z"/>
    </svg>

    <div class="holder">
      <p class="holder-name">Marcus Penhale</p>
      <p class="holder-role">Electrical Contractor</p>
    </div>

    <svg class="brand-mark" viewBox="0 0 1200 657" aria-label="Brightwire Power">
      <circle class="brand-dot" cx="413" cy="192" r="105"/>
      <text class="brand-name" x="21" y="402" textLength="788" lengthAdjust="spacingAndGlyphs">BRIGHTWIRE POWER</text>
    </svg>

    <p class="tagline">“Service when you need it”</p>

    <div class="contact">
      <p class="contact-phones">Tel:(08) 8456 3071 • Fax:(08) 8679 4315 • Mob:0438 562 740</p>
      <p class="contact-email">Email:marcus.penhale@brightwirepower.com.au</p>
      <p class="contact-web">Web: www.brightwirepower.com.au</p>
    </div>
  </main>
</body>
</html>
```